New corporate e-mail signature

We need a new e-mail signature for our company that is clean and professional. The requests are attached in a document.

Target Market(s)

CFO, CTO, Controllers, leaders, decision-makers.

Industry/Entity Type

Information Technology

Colors

Designer to choose colors to be used in the design.

Requirements
Must have
• See the PowerPoint document.
• - keep it as simple as possible.
• - same style as our new website design
• - It has to look good in all e-mail readers, and on all surfaces.
Nice to have
• - Please also attach 'best practise' for how to use the signature.
Should not have
• See the PowerPoint document. Use our color palette.
• - Do not include photo!

```html
<!DOCTYPE html>
<html lang="en">
<head>
<meta charset="utf-8">
<title>Ledgerwise e-mail signature</title>
<link rel="stylesheet" href="https://fonts.googleapis.com/css2?family=Carlito:wght@400;700&display=swap">
<style>
  :root {
    --navy: #0b3566;
    --blue: #2b8fd0;
    --teal: #1f6f95;
    --orange: #f0974a;
    --ink: #1b1b1b;
    --paper: #ffffff;
  }
  * { box-sizing: border-box; margin: 0; padding: 0; }
  html, body { width: 1200px; height: 330px; overflow: hidden; background: var(--paper); }
  .signature {
    position: relative;
    width: 1200px;
    height: 330px;
    overflow: hidden;
    font-family: "Carlito", "Calibri", sans-serif;
    color: var(--ink);
    background: var(--paper);
  }
  .brand-tab {
    position: absolute; left: 0; top: 0;
    width: 197px; height: 46px;
    background: linear-gradient(90deg, var(--navy), var(--blue));
    border-right: 3px solid var(--orange);
    border-bottom: 3px solid var(--orange);
    display: flex; align-items: center; justify-content: center;
  }
  .brand-name {
    color: var(--paper);
    font-weight: 700;
    font-size: 24px;
    letter-spacing: 0.2px;
  }
  .details {
    position: absolute; left: 25px; top: 86px;
    list-style: none;
    font-size: 21px;
    line-height: 39.5px;
  }
  .contact {
    position: absolute; left: 568px; top: 86px;
    list-style: none;
    font-size: 21px;
    line-height: 39.5px;
  }
  .contact li { display: flex; align-items: center; gap: 10px; }
  .contact svg { width: 25px; height: 25px; flex: none; }
  .follow {
    position: absolute; left: 19px; top: 257px;
    height: 44px;
    display: flex; align-items: center; gap: 16px;
    font-size: 21px;
  }
  .network { display: flex; align-items: center; gap: 7px; font-size: 18px; }
  .network-mark {
    width: 43px; height: 44px;
    background: var(--orange);
    flex: none;
  }
  .decor {
    position: absolute; right: 0; top: 125px;
    width: 165px; height: 197px;
    background: linear-gradient(160deg, rgba(31,111,149,0) 15%, rgba(31,111,149,0.35) 55%, rgba(31,111,149,0.75) 100%);
    clip-path: polygon(100% 0, 100% 100%, 0 100%);
  }
  .base-band {
    position: absolute; left: 0; bottom: 0;
    width: 1200px; height: 8px;
    background: linear-gradient(90deg, var(--navy), var(--navy) 55%, var(--blue));
  }
</style>
</head>
<body>
<div class="signature">
  <div class="brand-tab"><span class="brand-name">Ledgerwise</span></div>

  <ul class="details">
    <li>Name:</li>
    <li>Role:</li>
    <li>Company: Ledgerwise</li>
  </ul>

  <ul class="contact">
    <li>
      <svg viewBox="0 0 24 24" aria-hidden="true">
        <circle cx="12" cy="12" r="10.5" fill="none" stroke="var(--teal)" stroke-width="1.6"/>
        <path d="M8.6 6.8c.6-.4 1.2-.3 1.5.3l1 1.8c.3.5.1 1-.3 1.3l-.7.5c.5 1.5 1.4 2.7 2.7 3.6l.6-.6c.4-.4 1-.4 1.4 0l1.5 1.3c.5.4.5 1 .1 1.5-.8.9-1.8 1.2-2.9.7-2.7-1.3-4.6-3.6-5.5-6.5-.3-1.2.1-2.2.6-2.9z" fill="var(--teal)"/>
      </svg>
      <span>Mob:</span>
    </li>
    <li>
      <svg viewBox="0 0 24 24" aria-hidden="true">
        <rect x="1" y="5" width="22" height="15" fill="var(--teal)"/>
        <path d="M1.5 5.8 12 13.5 22.5 5.8" fill="none" stroke="var(--paper)" stroke-width="1.4"/>
      </svg>
      <span>Email:</span>
    </li>
    <li>
      <svg viewBox="0 0 24 24" aria-hidden="true">
        <g fill="none" stroke="var(--teal)" stroke-width="1.2">
          <circle cx="12" cy="12" r="10.5"/>
          <ellipse cx="12" cy="12" rx="4.5" ry="10.5"/>
          <path d="M2 8.5h20M2 15.5h20M12 1.5v21"/>
        </g>
      </svg>
      <span>www.ledgerwise.com</span>
    </li>
  </ul>

  <div class="follow">
    <span>Follow ledgerwise on:</span>
    <span class="network"><span class="network-mark"></span>Linkwork</span>
    <span class="network"><span class="network-mark"></span>Friendsite</span>
  </div>

  <div class="decor" role="img" aria-label="Decorative angular blue shard graphic"></div>
  <div class="base-band"></div>
</div>
</body>
</html>
```